Remote Computer Support PostCard

We need a Postcard Ad for marketing to businesses that need Remote Computer Support and Security. 2 sided and able to be mailed. Can be any color but color we use mostly is red. Remote Computer Support and Security per PC. Includes Remote Monitoring and Maintenance(RMM) Agent, Business Security Tools including Antivirus, Anti Malware, Ransomware Protection, Intrusion Prevention, Content Filtering and others. All remote support you need for $69.99 per pc per month.

Target Market(s)

All Businesses

Industry/Entity Type

Computer Support for Businesses

Colors
EB3D1F
EC4F4E
F09395
F8D3D4
FCEDEE

Requirements
Must have
• Bytharo, Inc. (555) 314-2968 . Sales@bytharo-example.com. Designed to be mailed. 6x9 Postcard Mailer Size Final 6.25" x 9" Ink & Bleed Four Color Process, Full Bleed Two Sides. Must have places for postage.
Nice to have
• Main lines should be in top 1/3 of postcard to stand out in mail.

```html
<!DOCTYPE html>
<html lang="en">
<head>
<meta charset="utf-8">
<title>Bytharo, Inc. – Remote Support Postcard</title>
<link rel="stylesheet" href="https://fonts.googleapis.com/css2?family=Oswald:wght@500;600;700&family=Roboto+Condensed:ital,wght@0,700;1,700&family=Roboto:wght@500;700&display=swap">
<style>
  :root{
    --red:#e8302b;
    --red-deep:#c9201c;
    --red-dark:#b01a17;
    --ink:#2a2a2c;
    --white:#ffffff;
    --photo-a:#3d4a5c;
    --photo-b:#6a7a8e;
    --blue:#1f86d6;
    --sky:#3aa6ee;
    --amber:#f4a51c;
  }
  *{margin:0;padding:0;box-sizing:border-box}
  html,body{width:1200px;height:833px;overflow:hidden;background:#fff}
  .card{position:relative;width:1200px;height:833px;overflow:hidden;background:var(--white);font-family:"Roboto Condensed",sans-serif}

  .header{position:absolute;left:0;top:0;width:1200px;height:144px;background:var(--white)}
  .brand{position:absolute;left:34px;top:52px;display:flex;align-items:center;gap:12px;white-space:nowrap}
  .brand-mark{width:30px;height:30px;background:var(--red)}
  .brand-name{font-family:"Roboto Condensed",sans-serif;font-weight:700;font-size:42px;color:var(--ink);letter-spacing:-0.5px}

  .tagline{position:absolute;left:370px;top:0;width:512px;height:84px;background:var(--red);
    clip-path:polygon(0 0,100% 0,100% 100%,3% 100%);
    color:var(--white);font-family:"Oswald",sans-serif;font-weight:700;font-size:33px;line-height:36px;
    text-align:center;padding-top:8px;padding-left:18px;white-space:nowrap}
  .subtag{position:absolute;left:362px;top:84px;width:486px;height:46px;background:var(--ink);
    clip-path:polygon(3% 0,100% 0,97% 100%,0 100%);
    color:var(--white);font-family:"Roboto Condensed",sans-serif;font-style:italic;font-weight:700;font-size:27px;
    line-height:46px;padding-left:30px;letter-spacing:0.3px;white-space:nowrap}

  .contact{position:absolute;left:888px;top:42px;width:306px;display:flex;flex-direction:column;gap:16px}
  .contact-row{display:flex;align-items:center;gap:12px;height:34px;color:var(--ink);font-family:"Roboto",sans-serif;font-weight:700;white-space:nowrap}
  .contact-row svg{width:34px;height:34px;flex:none}
  .phone{font-size:31px}
  .email{font-size:17px}

  .hero{position:absolute;left:0;top:144px;width:1200px;height:486px;
    background:linear-gradient(160deg,var(--photo-a) 0%,var(--photo-b) 55%,#4a586b 100%)}
  .hero-shade{position:absolute;inset:0;background:rgba(30,34,44,0.35)}

  .offer{position:absolute;left:0;top:168px;width:1200px;text-align:center;color:var(--white);
    font-family:"Oswald",sans-serif;font-weight:600;font-size:49px;line-height:56px;letter-spacing:1px;white-space:nowrap}
  .offer .price{color:var(--red)}
  .setup-note{position:absolute;left:0;top:352px;width:1200px;text-align:center;color:var(--white);
    font-family:"Roboto Condensed",sans-serif;font-style:italic;font-weight:700;font-size:22px}

  .feature{position:absolute;top:412px;width:260px;text-align:center;color:var(--white)}
  .feature-icon{display:block;margin:0 auto;width:104px;height:104px}
  .feature-label{margin-top:14px;font-family:"Roboto Condensed",sans-serif;font-weight:700;font-size:21px;line-height:23px;text-transform:uppercase;white-space:nowrap}
  .f1{left:46px}.f2{left:305px}.f3{left:611px}.f4{left:898px}

  .includes-band{position:absolute;left:0;top:630px;width:1200px;height:203px;background:var(--red)}
  .column{position:absolute;top:0;height:203px;text-align:center;color:var(--white)}
  .col-1{left:0;width:398px;background:var(--red)}
  .col-2{left:398px;width:416px;background:var(--red-deep)}
  .col-3{left:814px;width:386px;background:var(--red)}
  .column svg{display:block;margin:44px auto 0;width:62px;height:62px}
  .column-label{margin-top:14px;font-family:"Roboto Condensed",sans-serif;font-style:italic;font-weight:700;font-size:24px;line-height:28px;white-space:nowrap}
  .includes-tab{position:absolute;left:362px;top:610px;width:486px;height:42px;background:var(--ink);
    clip-path:polygon(3% 0,97% 0,100% 100%,0 100%);
    color:var(--white);font-family:"Roboto Condensed",sans-serif;font-style:italic;font-weight:700;font-size:27px;
    letter-spacing:11px;line-height:42px;text-align:center}
</style>
</head>
<body>
<main class="card">

  <header class="header">
    <div class="brand">
      <span class="brand-mark"></span>
      <span class="brand-name">Bytharo, Inc.</span>
    </div>
    <div class="tagline">FINALY, COMPUTER SECURITY<br>AND SUPPORT MADE EASY!</div>
    <div class="subtag">PERFECT FOR ANY SIZED BUSINESS</div>
    <div class="contact">
      <div class="contact-row phone">
        <svg viewBox="0 0 34 34"><circle cx="17" cy="17" r="15" fill="none" stroke="#2a2a2c" stroke-width="2.4"/><path d="M11.5 10c1.2-1 2.2-.8 2.8.3l1.3 2.4c.4.8.2 1.6-.5 2.1l-1 .7c.9 2 2.4 3.6 4.4 4.5l.8-1c.5-.7 1.3-.9 2.1-.5l2.4 1.3c1 .6 1.2 1.7.2 2.8-1.6 1.8-3.5 1.8-6 .5-3.2-1.7-5.6-4.4-7-7.7-.9-2.3-.9-4 .5-5.4z" fill="#2a2a2c"/></svg>
        <span>(555) 314-2968</span>
      </div>
      <div class="contact-row email">
        <svg viewBox="0 0 34 34"><circle cx="17" cy="17" r="15" fill="none" stroke="#2a2a2c" stroke-width="2.4"/><rect x="9" y="11.5" width="16" height="11" fill="none" stroke="#2a2a2c" stroke-width="2"/><path d="M9 11.5l8 6.5 8-6.5" fill="none" stroke="#2a2a2c" stroke-width="2"/></svg>
        <span>Sales@bytharo-example.com</span>
      </div>
    </div>
  </header>

  <section class="hero" role="img" aria-label="Close-up photo of a laptop keyboard in cool blue-grey light">
    <div class="hero-shade"></div>
  </section>

  <p class="offer">FOR ONLY <span class="price">$69.99</span> PER MONTH PER PC YOU GET<br>WORLD CLASS SECURITY SERVICES AND UNLIMITED<br>REMOTE TECHNICAL SUPPORT.</p>
  <p class="setup-note">*ONE TIME SETUP FEE OF $69.99 PER PC</p>

  <div class="feature f1">
    <svg class="feature-icon" viewBox="0 0 104 104"><circle cx="52" cy="52" r="50" fill="var(--blue)"/><path d="M34 48a18 18 0 0 1 32-10" fill="none" stroke="#fff" stroke-width="6" stroke-linecap="round"/><path d="M70 30v12H58" fill="none" stroke="#fff" stroke-width="6" stroke-linecap="round" stroke-linejoin="round"/><path d="M70 56a18 18 0 0 1-32 10" fill="none" stroke="#fff" stroke-width="6" stroke-linecap="round"/><path d="M34 74V62h12" fill="none" stroke="#fff" stroke-width="6" stroke-linecap="round" stroke-linejoin="round"/></svg>
    <p class="feature-label">Automated<br>System Updates</p>
  </div>
  <div class="feature f2">
    <svg class="feature-icon" viewBox="0 0 104 104"><circle cx="52" cy="52" r="50" fill="var(--sky)"/><path d="M68 24L52 48" stroke="#fff" stroke-width="6" stroke-linecap="round"/><path d="M44 44l18 12-10 22c-8-2-16-8-22-16z" fill="#fff"/><path d="M30 30l2 5 5 2-5 2-2 5-2-5-5-2 5-2z" fill="#fff"/></svg>
    <p class="feature-label">Automated<br>System Cleanup</p>
  </div>
  <div class="feature f3">
    <svg class="feature-icon" viewBox="0 0 104 104"><circle cx="52" cy="52" r="50" fill="var(--amber)"/><path d="M52 22l24 9v18c0 16-10 27-24 33-14-6-24-17-24-33V31z" fill="#fff"/><path d="M52 30l16 6v13c0 11-7 19-16 24z" fill="var(--amber)"/></svg>
    <p class="feature-label">Managed Antivirus<br>Including Ransomware<br>Detection and Protection</p>
  </div>
  <div class="feature f4">
    <svg class="feature-icon" viewBox="0 0 104 104"><circle cx="52" cy="52" r="50" fill="var(--red)"/><path d="M36 24h22l12 12v44H36z" fill="#fff"/><path d="M58 24v12h12" fill="#f8d3d4"/><path d="M42 46h22M42 54h22M42 62h22M42 70h14" stroke="var(--red)" stroke-width="3.5"/></svg>
    <p class="feature-label">Monthly Reports</p>
  </div>

  <section class="includes-band">
    <div class="column col-1">
      <svg viewBox="0 0 62 62" fill="none" stroke="#fff" stroke-width="2.6" stroke-linejoin="round"><rect x="6" y="10" width="50" height="34" rx="2"/><path d="M24 52h14M31 44v8"/><circle cx="31" cy="27" r="7"/><path d="M31 15v4M31 35v4M19 27h4M39 27h4M23 19l3 3M36 32l3 3M39 19l-3 3M26 32l-3 3"/></svg>
      <p class="column-label">Remote Monitoring and<br>Management Agent(RMM)</p>
    </div>
    <div class="column col-2">
      <svg viewBox="0 0 62 62" fill="none" stroke="#fff" stroke-width="2.6" stroke-linejoin="round" stroke-linecap="round"><rect x="6" y="10" width="50" height="34" rx="2"/><path d="M24 52h14M31 44v8"/><path d="M22 36l14-14M38 16a6 6 0 0 0-4 8l4 4a6 6 0 0 0 8-4l-4 0-3-3 0-4z"/></svg>
      <p class="column-label">Help Desk Application<br>on Desktop</p>
    </div>
    <div class="column col-3">
      <svg viewBox="0 0 62 62" fill="none" stroke="#fff" stroke-width="2.6" stroke-linejoin="round"><rect x="6" y="18" width="40" height="30" rx="2"/><path d="M18 18v-6h16v6M6 30h40"/><path d="M46 32l10 4v8c0 7-4 11-10 14-6-3-10-7-10-14v-8z" fill="var(--red)"/><path d="M42 44l3 3 6-6"/></svg>
      <p class="column-label">Vantrel Secure<br>Business Suite</p>
    </div>
  </section>
  <div class="includes-tab">INCLUDES</div>

</main>
</body>
</html>
```